New business card for civil engineering company - "Keystone Audit"

We need a business card designed for our new structural engineering company.

The company name is "Keystone Audit" logo files attached.

We would like the following:
* Two-sided card
* Simple design

Information to be placed on the card:
Name - Marcus Dellow
Job Title - Director / Structural Engineer
Credentials - BEng(Hons), CPEng, CMengNZ, IntPE(NZ)
Email - marcus.dellow@keystoneaudit.co.nz
mobile - 0219364058
website - www.keystoneaudit.co.nz

```html
<!DOCTYPE html>
<html lang="en">
<head>
<meta charset="utf-8">
<title>Keystone Audit – Business Card</title>
<link href="https://fonts.googleapis.com/css2?family=Open+Sans:wght@400;600;700&display=swap" rel="stylesheet">
<style>
  :root {
    --backdrop: #5a8ebd;
    --card: #ffffff;
    --card-shade: #f4f5f6;
    --ink: #3d3f42;
    --brand-blue: #3f7fc3;
    --rule: #5b7fb0;
    --icon: #3f7fc3;
  }
  * { margin: 0; padding: 0; box-sizing: border-box; }
  html, body {
    width: 1200px;
    height: 1101px;
    overflow: hidden;
  }
  body {
    background: var(--backdrop);
    font-family: "Open Sans", Arial, sans-serif;
    color: var(--ink);
    position: relative;
  }
  .card {
    position: absolute;
    left: 240px;
    width: 720px;
    height: 440px;
    background: linear-gradient(135deg, var(--card) 0%, var(--card-shade) 100%);
    box-shadow: 0 14px 30px rgba(20, 50, 90, 0.35);
  }
  .card--front { top: 80px; }
  .card--back { top: 580px; }

  .company-name {
    font-weight: 700;
    color: var(--ink);
    letter-spacing: 0.06em;
    text-transform: uppercase;
    display: flex;
    align-items: center;
    gap: 14px;
  }
  .company-name__dot {
    width: 14px;
    height: 14px;
    border-radius: 50%;
    background: var(--brand-blue);
  }
  .card--front .company-name {
    position: absolute;
    left: 0; right: 0;
    top: 190px;
    justify-content: center;
    font-size: 40px;
  }
  .card--back .company-name {
    position: absolute;
    left: 48px;
    bottom: 60px;
    font-size: 24px;
    gap: 10px;
  }
  .card--back .company-name__dot { width: 11px; height: 11px; }

  .contact {
    position: absolute;
    left: 360px;
    top: 70px;
    width: 320px;
  }
  .contact__name {
    font-size: 34px;
    font-weight: 600;
    color: var(--brand-blue);
    line-height: 1.1;
  }
  .contact__title {
    font-size: 19px;
    font-weight: 700;
    color: var(--ink);
    margin-top: 4px;
  }
  .contact__rule {
    border: 0;
    border-top: 1.5px solid var(--rule);
    margin: 16px 0 18px;
  }
  .contact__list { list-style: none; }
  .contact__item {
    display: flex;
    align-items: center;
    gap: 12px;
    font-size: 14px;
    line-height: 1;
    margin-bottom: 14px;
    white-space: nowrap;
  }
  .contact__icon {
    width: 16px;
    height: 16px;
    flex: 0 0 16px;
    fill: var(--icon);
  }
</style>
</head>
<body>

  <section class="card card--front" aria-label="Card front">
    <div class="company-name"><span class="company-name__dot"></span>Keystone Audit</div>
  </section>

  <section class="card card--back" aria-label="Card back">
    <div class="company-name"><span class="company-name__dot"></span>Keystone Audit</div>

    <div class="contact">
      <h1 class="contact__name">Marcus Dellow</h1>
      <p class="contact__title">Director / Structural Engineer</p>
      <hr class="contact__rule">
      <ul class="contact__list">
        <li class="contact__item">
          <svg class="contact__icon" viewBox="0 0 16 16" aria-hidden="true"><path d="M8 0a5.5 5.5 0 0 0-5.5 5.5C2.5 10 8 16 8 16s5.5-6 5.5-10.5A5.5 5.5 0 0 0 8 0zm0 8a2.5 2.5 0 1 1 0-5 2.5 2.5 0 0 1 0 5z"/></svg>
          BEng(Hons), CPEng, CMengNZ, IntPE(NZ)
        </li>
        <li class="contact__item">
          <svg class="contact__icon" viewBox="0 0 16 16" aria-hidden="true"><path d="M3.6 1 6 3.8 4.6 5.6c.9 2 2.6 3.7 4.6 4.7l1.7-1.5L14 11l-1.3 3c-6 0-11.6-5.5-11.6-11.6z"/></svg>
          0219364058
        </li>
        <li class="contact__item">
          <svg class="contact__icon" viewBox="0 0 16 16" aria-hidden="true"><path d="M1 3h14v10H1zM2 4.2v.4l6 4.3 6-4.3v-.4z"/></svg>
          marcus.dellow@keystoneaudit.co.nz
        </li>
        <li class="contact__item">
          <svg class="contact__icon" viewBox="0 0 16 16" aria-hidden="true"><path d="M8 1a7 7 0 1 0 0 14A7 7 0 0 0 8 1zm0 1.3c.7.6 1.4 1.9 1.7 3.7H6.3C6.6 4.2 7.3 2.9 8 2.3zM2.4 7.3h3.8a11 11 0 0 0 0 1.4H2.4a5.7 5.7 0 0 1 0-1.4zm5.6 6.4c-.7-.6-1.4-1.9-1.7-3.7h3.4c-.3 1.8-1 3.1-1.7 3.7zm1.8-5H6.2a11 11 0 0 1 0-1.4h3.6a11 11 0 0 1 0 1.4zm0 0zm0-2.7h3a5.7 5.7 0 0 1 0 0zm.2 1.3h3.8a5.7 5.7 0 0 1 0 1.4H10a11 11 0 0 0 0-1.4zM3 6a5.7 5.7 0 0 1 3.4-3.4C5.8 3.5 5.4 4.7 5.2 6zm7.6-3.4A5.7 5.7 0 0 1 13 6h-2.2c-.2-1.3-.6-2.5-1.2-3.4zM3 10h2.2c.2 1.3.6 2.5 1.2 3.4A5.7 5.7 0 0 1 3 10zm6.6 3.4c.6-.9 1-2.1 1.2-3.4H13a5.7 5.7 0 0 1-3.4 3.4z"/></svg>
          www.keystoneaudit.co.nz
        </li>
      </ul>
    </div>
  </section>

</body>
</html>
```